Residential Mortgage Leader needs Wordpress Design

Looking for a home page website design for a client. We develop using the WordPress platform and would prefer the design be at least loosely based on an existing WordPress template. Attached files have many notes from our creative brief with client. The site must be responsive. Approved, basic wireframe attached. There is room for interpretation.

Existing web site: http://www.marisolbrandt.example/

The Marisol Brandt Team relies on strong systems to deliver an on-time, done-right, friendly experience. Marisol offers mortgages and refinancing services throughout the United States. She is a successful Brindlemoor Lending agent who strives to be an active part of her community. She would like to focus the site on her team, rather than just her.

Difference makers...
When you work with the Marisol Brandt team you get a high level of expertise and a friendly experience.

She has amazing credentials. Marisol is widely recognized as a top producer for her company, and has earned a number of awards and honors for her customer service.

Marisol's team is very engaged and enjoys sharing social comments or photos from their community.

Imagery:
* Friendly, warm imagery, preferably of her team or an image to represent her team
* Clean and crisp
* Professional / Experts in mortgage and refinance
* Clean / Good use of white space
Updates

When possible, please use imagery from the DFW area. The client mentioned they would prefer not to see stock images. Thanks.

Amend that- creative use of stock images, however, is fine. A few designs have used stock imagery, but in a well-considered manner.

We added some photos and graphics that are local. We are Dallas / Ft. Worth, Plano, Frisco, Texas. We also added some examples of photos to use for the "In the Community" area. Stock photos of business folks just doesn't fit there. Thanks!

Target Market(s)

They service a lot of builders, but also work with homeowners. Their typical client is usually a woman searching for mortgage services online. She typically has a family and may refer her husband to Marisol's team. Keep in mind, however, they also see a number of other scenarios. Most of their clients are middle to high-end borrowers.

Industry/Entity Type

It Company

Requirements
Must have
• Design should be developed using program such as Photoshop or Fireworks or Illustrator as last preference. Ideally, the design would be based on an existing responsive WordPress theme, which we would customize. You must include the name of the target theme. The footer should include lots of space for disclaimers and legal language. Site navigation should include these choices: "Home, About, Builders, Mortgage Info, Approval, Blog, Contact"
Nice to have
• Blog, social media and photos area. Use of the already approved style prototype with colors and fonts (Lato- a Google font, Times New Roman and Cookie-a decorative Google font). However, we are open to interpretation.
Should not have
• Hard to read fonts or a lack of white space.

```html
<!DOCTYPE html>
<html lang="en">
<head>
<meta charset="utf-8">
<title>Brindlemoor Lending – Marisol Brandt Team</title>
<link href="https://fonts.googleapis.com/css2?family=Lato:wght@300;400;700;900&display=swap" rel="stylesheet">
<style>
:root{
  --red:#c41208;
  --red-dark:#a30d05;
  --ink:#333;
  --grey:#9a9a9a;
  --blue:#1a8fc0;
  --charcoal:#2b2b2b;
  --footer:#262626;
}
*{margin:0;padding:0;box-sizing:border-box}
html,body{width:1200px;height:1156px;overflow:hidden;background:#fff}
body{font-family:'Lato',sans-serif;color:var(--ink);position:relative}
.abs{position:absolute}

/* header */
.brand{left:200px;top:28px}
.brand-name{font-size:22px;font-weight:700;color:var(--red);letter-spacing:-.5px;display:flex;align-items:center;gap:8px}
.brand-name .mark{width:12px;height:12px;background:var(--red)}
.brand-sub{font-size:10px;font-weight:700;color:var(--ink);margin-top:2px}
.header-contact{right:200px;top:27px;text-align:right;font-size:14px;letter-spacing:-.4px}
.header-contact .phone{color:var(--red)}
.header-contact .mail{font-size:12.5px;margin-top:6px;color:var(--grey);letter-spacing:0}
.header-contact .mail b{color:var(--red);font-weight:400}

/* nav */
.nav{left:0;top:90px;width:1200px;height:45px;background:linear-gradient(#c81309,#b00f06);border-bottom:1px solid #fff;box-shadow:0 1px 0 var(--red)}
.nav ul{list-style:none;position:absolute;left:200px;top:0;display:flex;height:45px}
.nav li{font-size:13px;font-weight:700;color:#fff;line-height:39px;position:relative;text-align:center;padding-top:3px}
.nav li.active{background:var(--charcoal);height:45px}
.nav li + li::before{content:"";position:absolute;left:0;top:14px;height:12px;border-left:1px dotted rgba(255,255,255,.5)}

/* hero */
.hero-photo{left:200px;top:196px;width:362px;height:252px;background:linear-gradient(#e6ebf1 0,#c9d8e8 45%,#b4c8de 100%);border-radius:120px 120px 0 0}
.hero-title{left:601px;top:234px;font-size:36px;font-weight:900;color:var(--red);letter-spacing:-2.4px}
.hero-text{left:603px;top:276px;width:400px;font-size:14.5px;line-height:18px;letter-spacing:-.3px}
.btn{top:341px;height:33px;font-size:17px;font-weight:700;color:#fff;letter-spacing:-1px;display:flex;align-items:center}
.btn-start{left:603px;width:169px;background:linear-gradient(#555,#333)}
.btn-start span{padding-left:18px;width:132px}
.btn-start i{width:37px;height:33px;border-left:1px solid #777;display:flex;align-items:center;justify-content:center}
.or{left:780px;top:346px;font-size:18px;font-weight:700;color:var(--red)}
.or b{color:var(--ink)}
.btn-know{left:838px;width:153px;background:var(--red);justify-content:center;border:1px solid var(--red-dark)}
.dots{left:955px;top:427px;display:flex;gap:4px}
.dots i{width:8px;height:8px;border-radius:50%;background:#cfcfcf}
.dots i.on{background:var(--red)}
.shade{left:200px;width:800px;height:10px;background:radial-gradient(ellipse at 50% 0,rgba(0,0,0,.14),rgba(0,0,0,0) 70%)}

/* features */
.feature{top:494px;width:210px}
.feature h2{font-size:20px;font-weight:900;letter-spacing:-1.2px}
.feature h3{font-size:12px;font-weight:400;letter-spacing:-.4px;margin-top:1px}
.feature p{font-size:11px;line-height:13.6px;color:var(--grey);margin-top:10px}
.f-cred h2{color:var(--ink)} .f-award h2{color:var(--red)} .f-recog h2{color:var(--blue)}
.vrule{top:494px;height:100px;border-left:1px dotted #ddd}

/* community */
.section-title{left:0;width:1200px;top:674px;text-align:center;font-size:32px;font-weight:900;color:var(--red);letter-spacing:-2px}
.section-sub{left:0;width:1200px;top:711px;text-align:center;font-size:15px;font-weight:700;letter-spacing:-.8px}
.dash{left:230px;top:756px;width:740px;border-top:1px dashed #ccc}

.col-title{font-size:21px;font-weight:900;letter-spacing:-1.2px}
.blog{left:200px;top:784px}
.blog .col-title{display:flex;align-items:center;gap:3px;color:var(--ink)}
.blog ul{list-style:none;margin-top:10px}
.blog li{font-size:14px;color:var(--grey);line-height:24px;padding-left:13px;position:relative}
.blog li::before{content:"»";position:absolute;left:0;font-size:9px;color:#999}
.vrule2{left:376px;top:798px;height:165px;border-left:1px dotted #ddd}

.social{left:426px;top:786px;width:212px}
.social .col-title{color:var(--blue)}
.post{display:flex;gap:10px;padding:8px 0 6px;border-bottom:1px dashed #ccc}
.post:last-child{border:0}
.post .ico{width:18px;height:18px;border-radius:50%;background:#666;margin-top:6px;flex:none}
.post h4{font-size:11.5px;font-weight:700}
.post p{font-size:10.5px;line-height:13.5px;color:var(--grey)}

.community{left:689px;top:777px;width:311px;height:197px;background:var(--red)}
.community .col-title{color:#fff;position:absolute;left:27px;top:12px}
.thumbs{position:absolute;left:29px;top:49px;display:grid;grid-template-columns:repeat(3,80px);gap:10px 7px}
.thumb{height:53px;border:1px solid #e88;background:linear-gradient(#9bb3c9 0,#7a8c6b 45%,#5c7d3a 100%)}
.view-more{position:absolute;right:29px;top:171px;font-size:11px;font-weight:700;color:#fff}

/* footer */
.footer{left:0;top:1012px;width:1200px;height:144px;background:radial-gradient(ellipse at 50% 0,#353535,var(--footer) 70%)}
.portrait{left:201px;top:1037px;width:98px;height:93px;border:2px solid #777;background:linear-gradient(#6b5a4c,#3e3129)}
.agent{left:308px;top:1036px;color:#fff;width:195px}
.agent h5{font-size:18px;font-weight:400;letter-spacing:-.4px}
.agent .role{font-size:12px;font-weight:700;letter-spacing:-.3px}
.agent .nmls{font-size:10px;color:var(--red);margin-top:3px}
.agent p{font-size:10px;line-height:12.5px;color:#ccc}
.fvrule{top:1038px;height:96px;border-left:1px dotted #555}
.contact{left:579px;top:1036px;color:#fff}
.contact h5{font-size:18px;font-weight:400;letter-spacing:-.4px}
.contact .addr{display:flex;gap:9px;margin-top:6px}
.contact .badge{width:31px;height:29px;background:#fff;flex:none}
.contact .addr p{font-size:10.5px;line-height:13.5px;color:#ddd;letter-spacing:.3px}
.contact .circles{display:flex;gap:4px;margin-top:12px}
.contact .circles i{width:23px;height:23px;border-radius:50%;background:#bbb}
.fbrand{left:814px;top:1058px;color:#ccc}
.fbrand .name{font-size:18px;font-weight:700;color:#bbb}
.fbrand .sub{font-size:8px;font-weight:700;color:#aaa}
.fbrand p{font-size:10.5px;line-height:13.5px;margin-top:10px;letter-spacing:.3px}
</style>
</head>
<body>

<header>
  <div class="abs brand">
    <div class="brand-name">Brindlemoor Lending <span class="mark"></span></div>
    <div class="brand-sub">A Tallowbrook Capital Company</div>
  </div>
  <div class="abs header-contact">
    <div>Work With Us: <span class="phone">123 - 456 - 789</span></div>
    <div class="mail"><b>E-mail:</b> info@brindlemoorlending.example</div>
  </div>
</header>

<nav class="abs nav">
  <ul>
    <li class="active" style="width:78px">Home</li>
    <li style="width:95px">About</li>
    <li style="width:112px">Builders</li>
    <li style="width:147px">Mortgage Info</li>
    <li style="width:126px">Approval</li>
    <li style="width:100px">Blog</li>
    <li style="width:142px">Contact</li>
  </ul>
</nav>

<section class="hero">
  <div class="abs hero-photo" role="img" aria-label="Photo of the smiling mortgage team in light blue business shirts"></div>
  <h1 class="abs hero-title">EARNING YOUR BUSINESS</h1>
  <p class="abs hero-text">The Marisol Brandt Team relies on strong Systems to deliver an on-time, done-right &amp; friendly experience.</p>
  <div class="abs btn btn-start"><span>START HERE</span><i><svg width="12" height="16" viewBox="0 0 12 16"><path d="M1 1 L10 8 L1 15 Z" fill="none" stroke="#fff" stroke-width="2"/></svg></i></div>
  <div class="abs or"><b>-</b> OR <b>-</b></div>
  <div class="abs btn btn-know">Get to Know Us</div>
  <div class="abs dots"><i></i><i class="on"></i><i></i><i></i></div>
  <div class="abs shade" style="top:448px"></div>
</section>

<section>
  <div class="abs feature f-cred" style="left:200px">
    <h2>OUR CREDENTIALS</h2><h3>A top producer, top notch</h3>
    <p>Lorem ipsum dolor sit amet, consectetuer adi piscing elit, sed diam nonummy nibh emod tincidunt ut laoreet dolore magna erat volutpat.</p>
  </div>
  <div class="abs vrule" style="left:450px"></div>
  <div class="abs feature f-award" style="left:498px">
    <h2>AWARDS</h2><h3>Lorem ipsum dolor sit amet</h3>
    <p>Lorem ipsum dolor sit amet, consectetuer adi piscing elit, sed diam nonummy nibh emod tincidunt ut laoreet dolore magna erat volutpat.</p>
  </div>
  <div class="abs vrule" style="left:746px"></div>
  <div class="abs feature f-recog" style="left:794px">
    <h2>RECOGNION</h2><h3>Lorem ipsum dolor sit amet</h3>
    <p>Lorem ipsum dolor sit amet, consectetuer adi piscing elit, sed diam nonummy nibh emod tincidunt ut laoreet dolore magna erat volutpat.</p>
  </div>
  <div class="abs shade" style="top:641px"></div>
</section>

<section>
  <h2 class="abs section-title">ENGAGED IN OUR COMMUNITY</h2>
  <div class="abs section-sub">CONNECT WITH US</div>
  <div class="abs dash"></div>

  <div class="abs blog">
    <div class="col-title"><svg width="24" height="22" viewBox="0 0 24 22"><circle cx="4" cy="18" r="3.2" fill="#333"/><path d="M1 9a12 12 0 0 1 12 12M1 2a19 19 0 0 1 19 19" fill="none" stroke="#333" stroke-width="3.4"/></svg>BLOG</div>
    <ul>
      <li>Borrowing</li><li>Best Practices</li><li>Announcements</li><li>How to guides</li><li>Builder info</li><li>Resources</li>
    </ul>
  </div>
  <div class="abs vrule2"></div>

  <div class="abs social">
    <div class="col-title">SOCIAL</div>
    <div class="post"><i class="ico"></i><div><h4>Lorem ipsum dolor</h4><p>sit amet, consectetuer adipiscing elit, sed diam...</p></div></div>
    <div class="post"><i class="ico"></i><div><h4>Lorem ipsum dolor</h4><p>sit amet, consectetuer adipiscing elit, sed diam...</p></div></div>
    <div class="post"><i class="ico"></i><div><h4>Lorem ipsum dolor</h4><p>sit amet, consectetuer adipiscing elit, sed diam...</p></div></div>
  </div>

  <div class="abs community">
    <div class="col-title">IN THE COMMUNTY</div>
    <div class="thumbs">
      <div class="thumb" role="img" aria-label="Community festival crowd on a lawn"></div>
      <div class="thumb" role="img" aria-label="Outdoor community gathering"></div>
      <div class="thumb" role="img" aria-label="Community festival crowd on a lawn"></div>
      <div class="thumb" role="img" aria-label="Crowd at a local street event"></div>
      <div class="thumb" role="img" aria-label="Street fair with tents"></div>
      <div class="thumb" role="img" aria-label="Crowd at a local street event"></div>
    </div>
    <div class="view-more">view more...</div>
  </div>
</section>

<footer class="abs footer"></footer>
<div class="abs portrait" role="img" aria-label="Portrait of the branch manager"></div>
<div class="abs agent">
  <h5>Marisol Brandt</h5>
  <div class="role">Branch Manager</div>
  <div class="nmls">NMLS# 10482</div>
  <p>Lorem ipsum dolor sit amet, consect etuer adipiscing elit, sed diam nonum my nibh euismod tincidunt ut laoreet...</p>
</div>
<div class="abs fvrule" style="left:537px"></div>
<div class="abs contact">
  <h5>Contact Us</h5>
  <div class="addr"><i class="badge"></i><p>4820 Cedar Commons, Ste.<br>210 Maple Ridge, TX 75000</p></div>
  <div class="circles"><i></i><i></i><i></i></div>
</div>
<div class="abs fvrule" style="left:773px"></div>
<div class="abs fbrand">
  <div class="name">Brindlemoor Lending</div>
  <div class="sub">A Tallowbrook Capital Company</div>
  <p>Copyright © 2013 Brindlemoor Lending.<br>All Rights Reserved.</p>
</div>

</body>
</html>
```